DATA PROTECTION OFFICER - GENERAL DATA PROTECTION REGULATION

Our network of companies is called : KTV (GDPR-DPO ORLAX).
It is sourced and based in Brussels, Belgium, hosting the EU institutions : designers and enforcers of the GDPR (https://portal.vantreximo.example/info/law/privacy-rules_en).
We are setting up connected, empowered and visionary-interconnected organizations in each country, region or city concerned by the GDPR.
We have developed unique pedagogical methods, programs, instruments (video, softwares,…) and visionary training skills – initially and on a continuous basis – for the DPO & GDPR consultants.
Our motto is : From Challenges to Opportunities.
Our yearning is : developing soulful teams, join forces & talents with our clients.
Our most wanted reward : let us astonish you!
We opt for the best available softwares on the market for project management, data analytics, GDPR compliance, DPO assistance and in general : customer relation and enhanced communication between project members.
We contribute to bringing Artificial Intelligence and Data-Driven Mindsets in enterprises.
We perceive the GDPR as the best opportunity an organization faces to value its “gold” (its data) and offer the solutions to transform them into real-life currencies and assets… MONEY .
I guess my comments need time to be integrated and I provided a lot of text too! I would particularly encourage RW (UK) to take the best out of his several proposals to mix them in the best ONE website! Offering me many graphic elements to use for all my posts/pages... I am a prolix writer :)
Target Market(s)
SME's business leaders, HR and Legal departments, read : https://www.dailyquorvent.example/article/us-cyber-gdpr-dpo/growth-of-the-privacy-officer-role-in-firms-idQX8TR2LM4
Industry/Entity Type
Legal
Coding
Coded - Design and coding required
Number of Pages Required
5+ page
Colors
Designer to choose colors to be used in the design.
Requirements
Must have
- A HUMAN APPROACH
- WE NEED TO SEE HUMANS AND NOT ONLY ROBOTS OR ELECTRONIC DEVICES.
- 1) The DPO/GDPR Logos of the companies:
- https://files.pelmora.example/sh/a1b2c3d4e5f6g7h/AAX9kLmNpQrStUvWxYz0AbCd?dl=0
- https://files.pelmora.example/sh/h7g6f5e4d3c2b1a/AAY8jKlMnOpQrStUvWxYzAbC?dl=0 et DPO : https://files.pelmora.example/sh/q2w3e4r5t6y7u8i/AAZ7hIjKlMnOpQrStUvWxY-z?dl=0
- OR :
- https://files.pelmora.example/sh/z9x8c7v6b5n4m3l/AAW6gHiJkLmNoPqRsTuVwXyZ?dl=0
- AND :
- https://corvilanto.teamdrive.example/sites/all/_layouts/15/guestaccess.aspx?guestaccesstoken=Q4kdpx392MWTZ8RhbyN1Ka7m%2BTcqLwej5spK%2FmUnRQV%3D&folderid=2_7c31d90e24a815f96d02b4613e907a2fc&rev=1&e=9b271cd044716392c5207a44de8117a3
- 2) A surprising but human, clear, simple, white, lightning look!
- 3) WORDPRESS version so that I can edit easily and add text on existing and new pages
- We therefore pass each option and - even more so - through the sieve of this inevitable - and values-generating - ethical evaluation.
- In other words, we are doubly satisfied with EVERY solution:
- 1. As a DPO/consultant and advisor to commercial enterprises or non-profit organisations but necessarily entering into a relationship involving financial flows with the persons concerned; and
- 2. As concerned person: target of the actions envisaged, parent, child, citizen and avatar in our digital lives.
- We put personal data at the centre of our projects and internal meetings, and with clients, we therefore continue the stage of brainstorming, researching and visualising ideas in interaction with the Regulation, by analysing the ethical consequences of each option.
- We choose only solutions that are applicable to the greatest number and therefore satisfy us as citizens of an increasingly connected and digital world. We also see the Regulation as a commercial and marketing opportunity to enhance the value of personal data and develop the confidence of those concerned by respect and security in the processing of such data.
- Our ultimate test: we put ourselves in our children's shoes to test the option considered, then comment on it and evaluate it as a parent.
- NO TO INCOMPREHENSIVE LEGAL TERMS... It is simply prohibited from 25 May for all information to be communicated to the persons concerned by the Regulation!
Nice to have
- - Artificial Intelligence
- - Transhumans
- - Challenges becoming Opportunities
- - a Great Dame who Protects & Reassures (see GDPR logo)
- - Friendly communication - NOT too businesslike/cold/usual
- - Page content is available here in FRENCH then ENGLISH then DUTCH then GERMAN : https://files.pelmora.example/sh/k3j4h5g6f7d8s9a/AAV5fGhIjKlMnOpQrStUvWxY?dl=0
Should not have
- A cold, bankerlike, old economy, dull outlook

```html
<!DOCTYPE html>
<html lang="en">
<head>
<meta charset="utf-8">
<title>KTV – ORLAX</title>
<link rel="stylesheet" href="https://fonts.googleapis.com/css2?family=Nunito:wght@700;800&family=Open+Sans:wght@400;600;700&family=Saira+Condensed:wght@500&family=Source+Sans+3:wght@400&family=Montserrat:wght@600&display=swap">
<style>
  :root {
    --pink: #d6559e;
    --pink-bar: #cf5fa8;
    --yellow: #f8dc00;
    --ink: #1b1b1b;
    --white: #ffffff;
    --panel-blue: #3a4587;
    --panel-dark: #252525;
    --panel-indigo: #34449a;
    --panel-navy: #0d1230;
    --icon-core: #161a44;
    --ring: rgba(190,190,200,0.55);
    --footer-text: #333333;
  }
  * { margin: 0; padding: 0; box-sizing: border-box; }
  html, body { width: 1200px; height: 1122px; overflow: hidden; background: var(--white); }
  .page { position: relative; width: 1200px; height: 1122px; overflow: hidden; background: var(--white); }

  .hero-visual {
    position: absolute; left: 380px; top: 0; width: 820px; height: 780px;
    background:
      linear-gradient(to right, #ffffff 0%, rgba(255,255,255,0.6) 18%, rgba(255,255,255,0) 40%),
      radial-gradient(circle at 62% 52%, #f6c3e8 0%, #b86bd6 12%, #5a63d8 30%, #2b3a9e 52%, rgba(60,90,200,0.55) 72%, rgba(255,255,255,0) 92%),
      linear-gradient(160deg, #e9f0ff 0%, #c7d6ff 40%, #8aa7f2 100%);
  }

  .top-bar {
    position: absolute; left: 529px; top: 0; width: 671px; height: 42px;
    background: var(--pink-bar);
    clip-path: polygon(0 0, 100% 0, 100% 100%, 42px 100%);
    display: flex; align-items: center; padding-left: 76px;
    font-family: "Open Sans", sans-serif; font-weight: 700; font-size: 14.5px; color: var(--white);
    white-space: nowrap;
  }
  .contact-item { display: flex; align-items: center; gap: 8px; white-space: nowrap; }
  .contact-item + .contact-item { margin-left: 30px; }
  .contact-item svg { width: 22px; height: 22px; flex: none; }
  .social-list { display: flex; gap: 4px; margin-left: auto; }
  .social-dot { width: 20px; height: 20px; border: 1.6px solid var(--white); border-radius: 50%; }
  .lang { display: flex; align-items: center; gap: 6px; margin-left: 30px; margin-right: 25px; }
  .lang-dot { width: 16px; height: 16px; border-radius: 50%; background: #2a3f8f; border: 2px solid var(--white); }

  .brand { position: absolute; left: 23px; top: 42px; height: 90px; display: flex; align-items: center; gap: 30px; }
  .brand-mark { display: flex; align-items: center; gap: 10px; font-family: "Nunito", sans-serif; font-weight: 800; color: var(--pink); }
  .brand-mark .dot { width: 56px; height: 56px; border-radius: 50%; background: var(--pink); }
  .brand-mark .name { font-size: 30px; }
  .brand-sub { font-family: "Nunito", sans-serif; font-weight: 800; font-size: 30px; color: #3c3aa8; }

  .main-nav { position: absolute; right: 25px; top: 94px; display: flex; gap: 21px; font-family: "Montserrat", sans-serif; font-weight: 600; font-size: 13.4px; color: #1c1c1c; white-space: nowrap; }
  .main-nav a { color: inherit; text-decoration: none; padding-bottom: 6px; }
  .main-nav a.active { color: var(--pink); border-bottom: 3px solid var(--pink); }

  .hero-title { position: absolute; left: 26px; top: 252px; font-family: "Nunito", sans-serif; font-weight: 800; font-size: 29.5px; color: var(--pink); white-space: nowrap; }
  .hero-text { position: absolute; left: 26px; top: 313px; width: 470px; font-family: "Open Sans", sans-serif; font-size: 17px; line-height: 23.5px; color: var(--ink); }
  .btn-primary { position: absolute; left: 26px; top: 458px; width: 236px; height: 47px; background: var(--yellow); border-radius: 3px; display: flex; align-items: center; justify-content: center; font-family: "Open Sans", sans-serif; font-weight: 600; font-size: 19.5px; color: var(--ink); text-decoration: none; }

  .features { position: absolute; left: 0; top: 684px; width: 1200px; height: 398px; clip-path: polygon(0 0, 100% 68px, 100% 100%, 0 100%); display: flex; }
  .feature { position: relative; width: 300px; height: 100%; }
  .feature.about { background: var(--panel-blue); }
  .feature.services { background: var(--panel-dark); }
  .feature.schools { background: var(--panel-indigo); }
  .feature.ai { background: var(--panel-navy); }
  .feature h2 { position: absolute; left: 21px; top: 110px; font-family: "Saira Condensed", sans-serif; font-weight: 500; font-size: 21px; line-height: 26px; }
  .feature.about h2, .feature.schools h2 { color: var(--yellow); }
  .feature.services h2, .feature.ai h2 { color: var(--pink); }
  .feature p { position: absolute; left: 21px; top: 138px; width: 266px; font-family: "Source Sans 3", sans-serif; font-size: 16px; line-height: 20.8px; color: #e9eaf2; }
  .feature .more { position: absolute; left: 21px; top: 324px; width: 25px; height: 25px; }

  .feature-icon { position: absolute; width: 92px; height: 92px; border-radius: 50%; background: var(--ring); display: flex; align-items: center; justify-content: center; }
  .feature-icon span { width: 70px; height: 70px; border-radius: 50%; background: var(--icon-core); display: flex; align-items: center; justify-content: center; }
  .feature-icon svg { width: 36px; height: 36px; }

  .site-footer { position: absolute; left: 0; top: 1082px; width: 1200px; height: 40px; display: flex; align-items: center; justify-content: center; font-family: "Open Sans", sans-serif; font-weight: 600; font-size: 12.5px; color: var(--footer-text); }
</style>
</head>
<body>
<div class="page">
  <div class="hero-visual" role="img" aria-label="Illustration of a glowing digital human profile surrounded by network lines and data icons"></div>

  <div class="top-bar">
    <div class="contact-item">
      <svg viewBox="0 0 24 24" fill="none" stroke="#fff" stroke-width="1.6"><circle cx="12" cy="12" r="10.5"/><path d="M8.5 7.5c.6-.6 1.4-.5 1.8.1l.9 1.5c.3.5.2 1-.2 1.4l-.6.5c.5 1.2 1.4 2.1 2.6 2.6l.5-.6c.4-.4.9-.5 1.4-.2l1.5.9c.6.4.7 1.2.1 1.8-1 1-2.5 1.2-3.8.5-2-1.1-3.7-2.8-4.8-4.8-.7-1.3-.5-2.8.6-3.7z" fill="#fff" stroke="none"/></svg>
      +32 2 555 01 47
    </div>
    <div class="contact-item">
      <svg viewBox="0 0 24 24" fill="none" stroke="#fff" stroke-width="1.6"><circle cx="12" cy="12" r="10.5"/><rect x="6.5" y="8.5" width="11" height="7.5" rx="1"/><path d="M6.8 9l5.2 4 5.2-4"/></svg>
      info@orlax.example
    </div>
    <div class="social-list" aria-label="Social links">
      <span class="social-dot"></span><span class="social-dot"></span><span class="social-dot"></span>
    </div>
    <div class="lang"><span class="lang-dot"></span>EN
      <svg width="10" height="8" viewBox="0 0 10 8"><path d="M1 2l4 4 4-4" stroke="#fff" stroke-width="1.8" fill="none"/></svg>
    </div>
  </div>

  <div class="brand">
    <div class="brand-mark"><span class="dot"></span><span class="name">KTV</span></div>
    <div class="brand-sub">ORLAX</div>
  </div>

  <nav class="main-nav">
    <a class="active" href="#">HOME</a>
    <a href="#">ABOUT</a>
    <a href="#">SERVICES</a>
    <a href="#">OUR VISION</a>
    <a href="#">DPO SCHOOLS</a>
    <a href="#">AI &amp; SOFTWARES</a>
    <a href="#">CONTACT</a>
  </nav>

  <h1 class="hero-title">From Challenges to Opportunities</h1>
  <p class="hero-text">Sourced and based in Brussels, Belgium, hosting the EU institutions : designers and enforcers of the GDPR. We are setting up connected, empowered and visionary-interconnected organizations in each country, region or city concerned by the GDPR based on the TEAL approach .</p>
  <a class="btn-primary" href="#">Learn More</a>

  <section class="features">
    <article class="feature about">
      <h2>About</h2>
      <p>Lorem ipsum dolor sit amet, consec tetuer adipiscing elit, sed diam non ummy nibh euismod tincidunt ut lao reet dolore magna aliquam erat vol utpat. Ut wisi enim ad minim veniam, quis nostrud exerci tation ullamcor per suscipit lobortis nisl ut aliquip ex ea commodo consequat.</p>
      <svg class="more" viewBox="0 0 26 26"><circle cx="13" cy="13" r="12" fill="#f8dc00" stroke="#fff" stroke-width="2"/><path d="M7.5 13h10M13.5 9l4 4-4 4" stroke="#222" stroke-width="1.8" fill="none"/></svg>
    </article>
    <article class="feature services">
      <h2>Services</h2>
      <p>Lorem ipsum dolor sit amet, consec tetuer adipiscing elit, sed diam non ummy nibh euismod tincidunt ut lao reet dolore magna aliquam erat vol utpat. Ut wisi enim ad minim veniam, quis nostrud exerci tation.</p>
      <svg class="more" viewBox="0 0 26 26"><circle cx="13" cy="13" r="12" fill="#d6559e" stroke="#fff" stroke-width="2"/><path d="M7.5 13h10M13.5 9l4 4-4 4" stroke="#fff" stroke-width="1.8" fill="none"/></svg>
    </article>
    <article class="feature schools">
      <h2>DPO Schools</h2>
      <p>Lorem ipsum dolor sit amet, consec tetuer adipiscing elit, sed diam non ummy nibh euismod tincidunt ut lao reet dolore magna aliquam erat vol utpat. Ut wisi enim ad minim veniam, quis nostrud exerci tation ullamcor per suscipit lobortis.</p>
      <svg class="more" viewBox="0 0 26 26"><circle cx="13" cy="13" r="12" fill="#f8dc00" stroke="#fff" stroke-width="2"/><path d="M7.5 13h10M13.5 9l4 4-4 4" stroke="#222" stroke-width="1.8" fill="none"/></svg>
    </article>
    <article class="feature ai">
      <h2>AI &amp; Softwares</h2>
      <p>Lorem ipsum dolor sit amet, consec tetuer adipiscing elit, sed diam non ummy nibh euismod tincidunt ut lao reet dolore magna aliquam erat vol utpat. Ut wisi enim ad minim veniam, quis nostrud exerci tation ullamcor per suscipit.</p>
      <svg class="more" viewBox="0 0 26 26"><circle cx="13" cy="13" r="12" fill="#d6559e" stroke="#fff" stroke-width="2"/><path d="M7.5 13h10M13.5 9l4 4-4 4" stroke="#fff" stroke-width="1.8" fill="none"/></svg>
    </article>
  </section>

  <div class="feature-icon" style="left:117px; top:636px;"><span>
    <svg viewBox="0 0 36 36" fill="none" stroke="#fff" stroke-width="2"><rect x="5" y="5" width="11" height="11"/><rect x="18" y="5" width="11" height="11"/><rect x="5" y="18" width="11" height="11"/><path d="M22 20v12l3-3 3 5"/></svg>
  </span></div>
  <div class="feature-icon" style="left:417px; top:650px;"><span>
    <svg viewBox="0 0 36 36" fill="none" stroke="#fff" stroke-width="2"><path d="M18 6c-6 0-11 4-11 10 0 4 2 6 4 7v6h14v-6c2-1 4-3 4-7 0-6-5-10-11-10z"/><path d="M18 6v23M12 14h6M18 19h6"/></svg>
  </span></div>
  <div class="feature-icon" style="left:703px; top:664px;"><span>
    <svg viewBox="0 0 36 36" fill="none" stroke="#fff" stroke-width="2"><path d="M18 4l12 5v8c0 8-5 13-12 15C11 30 6 25 6 17V9z"/><path d="M18 8v20"/></svg>
  </span></div>
  <div class="feature-icon" style="left:1003px; top:683px;"><span>
    <svg viewBox="0 0 36 36" fill="none" stroke="#fff" stroke-width="2.4"><path d="M7 29l14-14M15 15l6 6M21 9l6 6M18 12l6 6"/></svg>
  </span></div>

  <footer class="site-footer">COPYRIGHT © 2018 ORLAX. ALL RIGHTS RESERVED.</footer>
</div>
</body>
</html>
```